Cover-Design für Buch über das Vater-Werden
Das Design hat genau die Beschreibung meines Briefings getroffen und mich sofort überzeugt. Die Idee war klasse.
Zielgruppe
Ich bin vor einem Jahr Vater geworden und habe spontan ein Buch über das Vater-Werden geschrieben. Die Zielgruppe sind also werdende Väter.
Aufgabenstellung
'Zwischen Wiege und Werkbank' ist ein smarter Ratgeber für werdende Väter. Er ist durchaus ernst gemeint, informativ und liefert Fakten. Aber er ist mit einem Augenzwinkern geschrieben und mit amüsanten Anekdoten untermalt, so dass der Ratgeber kurzweilig zu lessen ist. Das Buch behandelt die Zeitspanne vom Beginn bis zum Ende der Schwangerschaft. Zum besseren inhaltlichen Verständnis habe ich ein Exposé angehängt.

```html
<!DOCTYPE html>
<html lang="de">
<head>
<meta charset="utf-8">
<title>Zwischen Wiege und Werkbank – Buchcover</title>
<link rel="stylesheet" href="https://fonts.googleapis.com/css2?family=Teko:wght@400;500&display=swap">
<style>
  :root {
    --stage: #2c8a4e;
    --cover: #52b479;
    --title-blue: #1f5b95;
    --author-yellow: #e4dc6c;
    --art-teal: #2f9b8a;
    --art-blue: #3a6fa8;
    --art-yellow: #d9da74;
  }
  * { box-sizing: border-box; margin: 0; padding: 0; }
  html, body {
    width: 1200px;
    height: 1055px;
    overflow: hidden;
    background: var(--stage);
  }
  .stage {
    position: relative;
    width: 1200px;
    height: 1055px;
  }
  .front-cover {
    position: absolute;
    left: 250px;
    top: 68px;
    width: 610px;
    height: 920px;
    padding: 0 40px;
    background: var(--cover);
    display: flex;
    flex-direction: column;
    align-items: center;
    font-family: "Teko", "Arial Narrow", sans-serif;
    color: var(--title-blue);
  }
  .title {
    margin-top: 36px;
    display: flex;
    flex-direction: column;
    align-items: center;
    line-height: 0.84;
    font-weight: 500;
    text-transform: uppercase;
  }
  .title-line {
    font-size: 72px;
    letter-spacing: 0.22em;
    margin-right: -0.22em;
  }
  .title-line--large {
    font-size: 128px;
    letter-spacing: 0.03em;
    margin-right: -0.03em;
    margin-top: 6px;
  }
  .cover-art {
    margin-top: 24px;
    width: 300px;
    height: 400px;
    border-radius: 46% 40% 48% 42% / 30% 34% 44% 40%;
    background: radial-gradient(ellipse at 58% 40%, var(--art-yellow) 0%, var(--art-teal) 42%, var(--art-blue) 78%, transparent 100%);
    opacity: 0.85;
  }
  .author {
    margin-top: auto;
    margin-bottom: 36px;
    font-size: 56px;
    font-weight: 500;
    line-height: 1;
    color: var(--author-yellow);
    letter-spacing: 0.01em;
  }
  .spine {
    position: absolute;
    left: 930px;
    top: 68px;
    width: 96px;
    height: 920px;
    background: var(--cover);
    display: flex;
    justify-content: center;
    padding-top: 40px;
    font-family: "Teko", "Arial Narrow", sans-serif;
    font-weight: 500;
    text-transform: uppercase;
  }
  .spine-text {
    writing-mode: vertical-rl;
    font-size: 52px;
    line-height: 1;
    white-space: nowrap;
  }
  .spine-title { color: var(--author-yellow); }
  .spine-author { color: var(--title-blue); margin-top: 40px; }
</style>
</head>
<body>
<main class="stage">
  <section class="front-cover">
    <h1 class="title">
      <span class="title-line">Zwischen</span>
      <span class="title-line">Wiege und</span>
      <span class="title-line title-line--large">Werkbank</span>
    </h1>
    <div class="cover-art" role="img" aria-label="Aquarell-Illustration eines Seepferdchens in Blau, Türkis und Gelb"></div>
    <p class="author">TOBIAS KELSCH</p>
  </section>
  <aside class="spine">
    <p class="spine-text">
      <span class="spine-title">Zwischen Wiege und Werkbank</span>
      <span class="spine-author">Tobias Kelsch</span>
    </p>
  </aside>
</main>
</body>
</html>
```